Young and modern Electrical company working in the commercial arena.

Wanting a business card design thats modern and will last. Maybe Minimalist? Happy to look at changing my logo

Target Market(s)

Builders, Project Managers

Industry/Entity Type

Electrical

Contact Information for Business Card

Name
Address
Phone number
Job title

Logo Text

our name or just the logo i'm open to ideas

Font styles to use
Sans Serif

Requirements
Nice to have
• would like to keep the purple in our current logo. it's kinda unique to our market
Should not have
• Don't want it to be to busy. simple is best i think

```html
<!DOCTYPE html>
<html lang="en">
<head>
<meta charset="utf-8">
<title>Halden Electrical – Business Card</title>
<link rel="stylesheet" href="https://fonts.googleapis.com/css2?family=Arimo:wght@400&display=swap">
<style>
  :root {
    --card-bg: #ffffff;
    --facet-light: #fefefe;
    --facet-shade: #f6f7f8;
    --brand-mark: #5a4cf6;
    --accent-cyan: #00e1f8;
  }
  * { margin: 0; padding: 0; box-sizing: border-box; }
  html, body {
    width: 1200px;
    height: 720px;
    overflow: hidden;
    background: var(--card-bg);
  }
  .card {
    position: relative;
    width: 1200px;
    height: 720px;
    overflow: hidden;
    font-family: "Arimo", Arial, sans-serif;
    font-weight: 400;
  }
  .card__texture {
    position: absolute;
    inset: 0;
    background: linear-gradient(135deg, var(--facet-light) 0%, var(--facet-shade) 45%, var(--facet-light) 70%, var(--facet-shade) 100%);
  }
  .brand-mark {
    position: absolute;
    left: 70px;
    top: 222px;
    width: 520px;
    height: 52px;
    display: flex;
    justify-content: center;
    align-items: center;
    gap: 16px;
    white-space: nowrap;
  }
  .brand-mark__square {
    width: 20px;
    height: 20px;
    background: var(--brand-mark);
  }
  .brand-mark__name {
    font-size: 44px;
    line-height: 1;
    color: var(--brand-mark);
  }
  .company-name {
    position: absolute;
    left: 332px;
    top: 342px;
    transform: translateX(-50%) scaleX(0.64);
    font-size: 76px;
    font-weight: 400;
    color: var(--accent-cyan);
    white-space: nowrap;
    line-height: 1;
  }
  .divider {
    position: absolute;
    left: 596px;
    top: 153px;
    width: 6px;
    height: 413px;
    border-radius: 3px;
    background: var(--accent-cyan);
  }
  .contact {
    position: absolute;
    left: 0;
    top: 0;
    color: var(--accent-cyan);
    list-style: none;
  }
  .contact__item {
    position: absolute;
    white-space: nowrap;
    line-height: 1;
  }
  .contact__item--name { left: 615px; top: 268px; font-size: 38px; }
  .contact__item--address { left: 609px; top: 340px; font-size: 41px; }
  .contact__item--phone { left: 609px; top: 411px; font-size: 36px; }
  .contact__item--title { left: 611px; top: 476px; font-size: 36px; }
</style>
</head>
<body>
  <main class="card">
    <div class="card__texture" role="img" aria-label="Faint light grey low-poly faceted background texture"></div>

    <div class="brand-mark">
      <span class="brand-mark__square"></span>
      <span class="brand-mark__name">Halden Electrical</span>
    </div>

    <h1 class="company-name">Halden Electrical</h1>

    <div class="divider"></div>

    <ul class="contact">
      <li class="contact__item contact__item--name">Name</li>
      <li class="contact__item contact__item--address">Address</li>
      <li class="contact__item contact__item--phone">Phone #</li>
      <li class="contact__item contact__item--title">Job Title</li>
    </ul>
  </main>
</body>
</html>
```